Shipping cards

Expedited delivery of various business related products , packages ,parcels etc. Intrastate or Interstate.

Target Market(s)

business and or private customer base.with expedited needs and short term or long term needs.

Industry/Entity Type

Business

Contact Information for Business Card

would like the silhouette of my dog between the business name Amber{ } Fox . Amber Fox Freight ,Expedited Delivery, tel330-958-3637 fax TBD , dispatch@quillmail.test, Dennis J. Holt- Owner

Font styles to use
Serif

Requirements
Must have
• dog silhouette between Amber Fox or before and after name of company.
Should not have
• remove oval from silhouette around dog

```html
<!DOCTYPE html>
<html lang="en">
<head>
<meta charset="utf-8">
<title>Amber Fox Freight – Business Card</title>
<link rel="stylesheet" href="https://fonts.googleapis.com/css2?family=Cabin:wght@400;600&family=Barlow+Semi+Condensed:wght@700&family=Playfair+Display:wght@700&display=swap">
<style>
  :root {
    --card-bg: #b3b3b3;
    --ink: #1e1e1e;
    --accent-red: #ff0000;
    --icon-grey: #555555;
  }
  * { margin: 0; padding: 0; box-sizing: border-box; }
  html, body {
    width: 1200px;
    height: 686px;
    overflow: hidden;
    background: var(--card-bg);
  }
  .card {
    position: relative;
    width: 1200px;
    height: 686px;
    background: var(--card-bg);
    color: var(--ink);
    font-family: "Cabin", sans-serif;
  }
  .brand-mark {
    position: absolute;
    left: 540px;
    top: 60px;
    width: 132px;
    height: 132px;
  }
  .brand-word {
    position: absolute;
    top: 136px;
    font-family: "Playfair Display", serif;
    font-weight: 700;
    font-size: 56px;
    line-height: 70px;
    color: var(--ink);
    white-space: nowrap;
  }
  .brand-word--first {
    right: 662px;
  }
  .brand-word--second {
    left: 676px;
  }
  .brand-sub {
    position: absolute;
    left: 0;
    top: 202px;
    width: 1180px;
    text-align: center;
    font-family: "Playfair Display", serif;
    font-weight: 700;
    font-size: 34px;
    line-height: 44px;
    letter-spacing: 4px;
    color: var(--ink);
  }
  .tagline {
    position: absolute;
    left: 0;
    top: 325px;
    width: 1200px;
    text-align: center;
    font-family: "Barlow Semi Condensed", sans-serif;
    font-weight: 700;
    font-size: 64px;
    line-height: 64px;
    color: var(--accent-red);
  }
  .contact {
    position: absolute;
    left: 181px;
    top: 442px;
    font-size: 40px;
    line-height: 52px;
    letter-spacing: 0.5px;
  }
  .contact-phone { position: relative; }
  .phone-icon {
    position: absolute;
    left: -36px;
    top: 10px;
    width: 22px;
    height: 34px;
  }
  .person {
    position: absolute;
    left: 876px;
    top: 444px;
    transform: translateX(-50%);
    text-align: center;
    white-space: nowrap;
  }
  .person-name {
    font-size: 40px;
    line-height: 48px;
    letter-spacing: 5px;
    text-transform: uppercase;
  }
  .person-role {
    font-size: 39px;
    line-height: 46px;
  }
</style>
</head>
<body>
  <main class="card">
    <header class="brand" aria-label="Amber Fox Freight">
      <span class="brand-word brand-word--first">Amber</span>
      <svg class="brand-mark" viewBox="0 0 132 132" aria-hidden="true">
        <circle cx="66" cy="66" r="64" fill="var(--accent-red)"/>
      </svg>
      <span class="brand-word brand-word--second">Fox</span>
      <div class="brand-sub">FREIGHT</div>
    </header>

    <h1 class="tagline">EXPEDITED DELIVERY</h1>

    <section class="contact">
      <div class="contact-phone">
        <svg class="phone-icon" viewBox="0 0 22 34" aria-hidden="true">
          <rect x="1" y="4" width="20" height="29" rx="4" fill="var(--icon-grey)"/>
          <rect x="3" y="0" width="3" height="6" rx="1" fill="var(--icon-grey)"/>
          <rect x="5" y="8" width="12" height="9" rx="1" fill="var(--card-bg)"/>
        </svg>
        412.573.2916
      </div>
      <div class="contact-fax">fax TBD</div>
      <div class="contact-email">dispatch@quillmail.test</div>
    </section>

    <section class="person">
      <div class="person-name">Dennis J Holt</div>
      <div class="person-role">Owner</div>
    </section>
  </main>
</body>
</html>
```